Fashion Site

I need a Home Page and one Internal Page (About or Stores you choose) for a Fashion Retailer called VERANO based in Melbourne Australia. Their product range is high end - European brand (i.e. Corvelli, Batrano etc) shoes, handbags and accessories for Women and Men (Customers 75% Women 25% Men). They currently have a site at www.verano-shoes.com.au (My developer will take this design and push it through the rest of the site).

The new design will be clean and modern and reflect the high end brands they sell. The finished site will have the home page plus the following pages - About - Stores - News/Sales - E-Shop - Contact with links to Join our mail list - Chatterly - Pixelane. I would like a main banner/slider at the top that will have 6 sliding images - through these images I would like to reinforce the following - the products are imported direct from Italy and are the latest most current designs from leading fashion houses (women and men) - A Modern Look with an Italian feel. Then we would also like to show some products/specials from the new E-Shop on the home page as well as the usual links etc.

Their colours are black and white but I am open to having a splash of colour and a must is to use the photography supplied in a creative way (see http://dunestrive.com as an Idea), we want to show that the products are high end - hand made. Their end/tag line is Ever Poised. We DO NOT want any brand names mentioned/Listed (if on a photo that is fine). The site will need to be easy to navigate and google friendly so please keep this in mind with the design. The images supplied include: Product Shots, Melbourne Stores, Italy Warehouse (2 story building with red roof) and Italy Factories/Craftsmen.

Target Market(s)

Fashion Conscious Women and Men who like the finer things in life

Industry/Entity Type

Fashion

Font styles to use
Serif
Sans Serif

Requirements
Must have
• Top Banner with 6 Images that Slide/Scroll in a banner.
Nice to have
• See the Following Sites that may inspire:
https://www.koti.com.au
http://www.fennicraft.co (the Look not the colours)
http://www.tobsandyou.com
Also Like the banner in this http://dunestrive.com (Just the banner)

```html
<!DOCTYPE html>
<html lang="en">
<head>
<meta charset="utf-8">
<title>VERANO — Home</title>
<link href="https://fonts.googleapis.com/css2?family=Playfair+Display:wght@700&family=Cinzel:wght@400&family=Open+Sans:wght@400;600;700&display=swap" rel="stylesheet">
<style>
:root{
  --red:#c8102e;
  --ink:#222;
  --muted:#777;
  --nav:#8f949b;
  --nav-dark:#5d636b;
  --panel:#f1f1f1;
  --footer:#ebebeb;
  --rule:#d6d6d6;
  --white:#fff;
}
*{margin:0;padding:0;box-sizing:border-box}
html,body{width:683px;height:1200px;overflow:hidden;background:var(--white)}
body{font-family:"Open Sans",Arial,sans-serif;color:var(--ink);font-size:9px;position:relative}
.hero{position:absolute;top:0;left:0;width:683px;height:410px;overflow:hidden;
  background:radial-gradient(ellipse at 70% 80%,#7b4a3c 0%,rgba(60,50,55,0) 45%),linear-gradient(160deg,#3c4250 0%,#1f232c 55%,#2b2a30 100%)}
.hero-wordmark{position:absolute;left:40px;top:30px;width:600px;text-align:left;white-space:nowrap;font-family:"Playfair Display",serif;font-weight:700;font-size:132px;letter-spacing:1px;color:rgba(214,220,232,.78);line-height:1}
.hero-tagline{position:absolute;left:62px;top:220px;font-family:"Cinzel",serif;font-size:31px;line-height:1.25;color:#e9ecf2;letter-spacing:1px}
.nav{position:absolute;top:410px;left:0;width:683px;height:30px;background:linear-gradient(#a2a7ad,var(--nav));display:flex;align-items:center;padding-left:45px}
.nav a{color:#fff;text-decoration:none;font-size:10px;padding:0 12px;height:30px;line-height:30px;white-space:nowrap}
.nav a.active{background:var(--nav-dark)}
.nav-tools{margin-left:auto;margin-right:45px;display:flex;gap:4px}
.nav-tools span{width:26px;height:22px;background:var(--nav-dark);display:flex;align-items:center;justify-content:center}
.promos{position:absolute;top:466px;left:45px;width:593px;display:flex;gap:14px}
.promo{width:188px;height:122px;position:relative;display:flex;align-items:center;justify-content:center}
.promo-women{background:linear-gradient(135deg,#5d8cc4,#c9d9ec)}
.promo-acc{background:linear-gradient(135deg,#6d5a48,#c2a98a)}
.promo-men{background:linear-gradient(135deg,#4f86b5,#9fc0d6)}
.promo-label{background:rgba(20,20,20,.82);color:#fff;text-align:center;padding:7px 14px;font-size:10px;font-weight:700;line-height:1.3;text-transform:uppercase}
.promo-label b{display:block;background:var(--white);color:var(--ink);font-size:8px;margin-top:5px;padding:2px 4px}
.tabs{position:absolute;top:598px;left:45px;width:593px;height:22px;border-bottom:1px solid var(--rule);display:flex;align-items:flex-end}
.tabs span{font-size:10px;font-weight:600;padding:0 10px 5px 0;margin-right:8px}
.tabs span.active{border-bottom:2px solid var(--red)}
.tabs .arrows{margin-left:auto;display:flex;gap:3px;padding-bottom:5px}
.tabs .arrows i{width:12px;height:12px;border:1px solid #aaa;border-radius:50%;display:block}
.grid{position:absolute;top:636px;left:45px;width:593px;display:grid;grid-template-columns:repeat(4,130px);column-gap:24px;row-gap:22px}
.product{text-align:center}
.product-photo{height:126px;border:1px solid #e2e2e2}
.product-name{font-size:9px;margin-top:8px}
.product-price{font-size:9px;font-weight:700;margin-top:4px}
.product.featured{background:#e6e6e6}
.product.featured .product-photo{border:none;display:flex;flex-direction:column;align-items:center;justify-content:center;gap:5px;background:#eeeeee}
.featured .badge{width:28px;height:28px;border-radius:50%;background:#8a93a8}
.featured .action{font-size:7px;background:#fff;width:96px;padding:3px 0;text-transform:uppercase}
.product.featured .product-name,.product.featured .product-price{background:#8a93a8;color:#fff;margin:0;padding:4px 0}
.footer{position:absolute;top:1020px;left:0;width:683px;height:140px;background:var(--footer);padding:14px 45px 0;display:flex;gap:28px}
.footer-col{width:130px}
.footer-col h4{color:var(--red);font-size:9px;font-weight:700;margin-bottom:6px;letter-spacing:.5px}
.footer-col li{list-style:none;font-size:7px;line-height:1.7;color:#444;padding-left:8px;position:relative}
.footer-col li::before{content:"";position:absolute;left:0;top:5px;width:3px;height:3px;background:var(--red)}
.footer-col p{font-size:7px;line-height:1.55;color:#555}
.signup{display:flex;margin-top:8px}
.signup span{flex:1;height:16px;background:#fff;border:1px solid #ccc;font-size:7px;color:#999;padding:3px 4px}
.signup b{width:20px;height:16px;background:var(--red);color:#fff;font-size:7px;text-align:center;line-height:16px}
.icons{display:flex;gap:4px;margin-top:6px}
.icons i{width:14px;height:14px;border-radius:50%;background:#6c7380;display:block}
.cards{display:flex;gap:3px;margin-top:5px}
.cards i{width:18px;height:11px;background:#9aa1ab;display:block}
.bottom{position:absolute;top:1160px;left:0;width:683px;height:40px;background:#e0e0e0;display:flex;align-items:center;padding:0 45px;gap:14px}
.bottom-name{font-family:"Open Sans",sans-serif;font-weight:700;font-size:12px;color:#555}
.bottom p{font-size:7px;color:#666;line-height:1.5}
</style>
</head>
<body>
<header class="hero" role="img" aria-label="Banner photograph of a woman in red high heels and a man's dark trousers, fashion scene">
  <div class="hero-wordmark">VERANO</div>
  <div class="hero-tagline">EVER<br>POISED</div>
</header>

<nav class="nav">
  <a class="active">Home</a><a>About Us</a><a>Stores</a><a>News/Sales</a><a>Contact Us</a><a>Join Mail List</a>
  <div class="nav-tools">
    <span><svg width="12" height="12" viewBox="0 0 12 12"><path d="M1 2h2l1.5 6h6l1-4H4" fill="none" stroke="#fff" stroke-width="1.2"/><circle cx="5" cy="10.5" r="1" fill="#fff"/><circle cx="9.5" cy="10.5" r="1" fill="#fff"/></svg></span>
    <span><svg width="12" height="12" viewBox="0 0 12 12"><circle cx="5" cy="5" r="3.5" fill="none" stroke="#fff" stroke-width="1.4"/><path d="M7.6 7.6L11 11" stroke="#fff" stroke-width="1.6"/></svg></span>
  </div>
</nav>

<section class="promos">
  <div class="promo promo-women" role="img" aria-label="Woman in a blue dress, women's collection"><div class="promo-label">Women's<br>Collection<b>SHOP NOW</b></div></div>
  <div class="promo promo-acc" role="img" aria-label="Store interior with handbags on shelves"><div class="promo-label">New<br>Accessory</div></div>
  <div class="promo promo-men" role="img" aria-label="Men's shoes photographed by the sea"><div class="promo-label">Men's<br>Collection</div></div>
</section>

<div class="tabs">
  <span class="active">New arrivals</span><span>Popular</span><span>Best Sellers</span>
  <div class="arrows"><i></i><i></i></div>
</div>

<section class="grid">
  <div class="product featured">
    <div class="product-photo"><div class="badge"></div><div class="action">Add to compare</div><div class="action">Add to wishlist</div></div>
    <div class="product-name">Lorem ipsum dolor sit</div><div class="product-price">$265.15</div>
  </div>
  <div class="product"><div class="product-photo" role="img" aria-label="Black and white ballet flats" style="background:linear-gradient(#f4f4f4,#cfcfcf)"></div><div class="product-name">Lorem ipsum dolor sit</div><div class="product-price">$265.15</div></div>
  <div class="product"><div class="product-photo" role="img" aria-label="Blue and red leather loafers" style="background:linear-gradient(135deg,#f5f5f5 30%,#3c78c0 55%,#c23b2e 80%)"></div><div class="product-name">Lorem ipsum dolor sit</div><div class="product-price">$265.15</div></div>
  <div class="product"><div class="product-photo" role="img" aria-label="Teal suede driving loafer" style="background:linear-gradient(135deg,#f2f2f2 30%,#2f8c96 60%,#e9e9e9)"></div><div class="product-name">Lorem ipsum dolor sit</div><div class="product-price">$265.15</div></div>
  <div class="product"><div class="product-photo" role="img" aria-label="Coral red pumps" style="background:linear-gradient(135deg,#f3f3f3 25%,#e8553f 55%,#efefef)"></div><div class="product-name">Lorem ipsum dolor sit</div><div class="product-price">$265.15</div></div>
  <div class="product"><div class="product-photo" role="img" aria-label="Pink and red flat sandals" style="background:linear-gradient(135deg,#f4f4f4 30%,#e3777c 60%,#f0f0f0)"></div><div class="product-name">Lorem ipsum dolor sit</div><div class="product-price">$265.15</div></div>
  <div class="product"><div class="product-photo" role="img" aria-label="Black sequined slip-on shoes" style="background:linear-gradient(135deg,#f2f2f2 30%,#2a2a2e 60%,#ececec)"></div><div class="product-name">Lorem ipsum dolor sit</div><div class="product-price">$265.15</div></div>
  <div class="product"><div class="product-photo" role="img" aria-label="White leather lace-up shoes" style="background:linear-gradient(135deg,#d9d6cc,#f5f3ee)"></div><div class="product-name">Lorem ipsum dolor sit</div><div class="product-price">$265.15</div></div>
</section>

<footer class="footer">
  <div class="footer-col"><h4>INFORMATION</h4><ul><li>About Us</li><li>Delivery Information</li><li>Privacy Policy</li><li>Terms &amp; Conditions</li></ul></div>
  <div class="footer-col"><h4>MY ACCOUNT</h4><ul><li>My Account</li><li>Wish List</li><li>Brands</li><li>Specials</li><li>Secure payment</li></ul></div>
  <div class="footer-col"><h4>NEWSLETTER SIGNUP</h4><p>Lorem ipsum dolor sit amet, consectetur adipiscing elit, sed do eiusmod tempor incididunt ut labore et dolore magna aliqua.</p><div class="signup"><span>Email</span><b>GO</b></div></div>
  <div class="footer-col"><h4>GET IN TOUCH</h4><p>Phone: 1-300-555-014<br>Email: hello@verano-shoes.com.au<br>Verano Retail Pty Ltd<br>Street Name, Melbourne VIC</p>
    <div class="icons"><i></i><i></i><i></i><i></i><i></i></div>
    <div class="cards"><i></i><i></i><i></i><i></i><i></i></div>
  </div>
</footer>
<div class="bottom">
  <span class="bottom-name">VERANO</span>
  <p>Copyright © 2014 Verano. All rights reserved.<br>Ever Poised</p>
</div>
</body>
</html>
```